Webdesign für Holding-Firma
Zielgruppe
Die velunto Holding ist eine Holding-Firma mit drei Tochtergesellschaften: velunto trusted advisors, velutno Real estate und Velunto GmbH. Wir haben Beteiligungen in IT-Unternehmen, Real Estate sowie kleine und mittlere Startups.
Aufgabenstellung
Das Design sollte nicht zu bunt sein und eher schlicht und futuristisch gestaltet sein. Gerne können die Farben aus den verschiedenen Logos verarbeitet werden.

```html
<!DOCTYPE html>
<html lang="de">
<head>
<meta charset="utf-8">
<title>velunto Holding – Webdesign</title>
<link href="https://fonts.googleapis.com/css2?family=Hind:wght@400;500;600;700&display=swap" rel="stylesheet">
<style>
:root{
  --ink:#1b1b1b;
  --muted:#444;
  --line:#d9d9d9;
  --tile:#e6e6e6;
  --panel:#f1f1f1;
  --facet:#f4f4f4;
  --green:#7ed43c;
  --lime:#d6ec2b;
  --red:#e8412a;
  --orange:#f4a522;
  --sky1:#9fc2ea;
  --sky2:#c9dcf2;
  --facade:#6d6560;
  --aerial1:#6c8a4e;
  --aerial2:#a79b82;
}
*{margin:0;padding:0;box-sizing:border-box}
html,body{width:693px;height:1200px;overflow:hidden;background:#fff}
body{font-family:"Hind",Arial,sans-serif;color:var(--ink);position:relative}
.screen{position:absolute;left:151px;top:58px;width:391px;height:252px;background:#fff;border:1px solid var(--line);overflow:hidden}
.facets{position:absolute;inset:0;pointer-events:none}
.brand{position:absolute;display:flex;align-items:center;gap:4px;font-weight:600;color:var(--ink);white-space:nowrap}
.brand i{display:block;background:var(--green)}
.lang{position:absolute;font-size:5.5px;display:flex;align-items:center;gap:5px}
.burger{width:11px;height:7px;border-top:1.3px solid #666;border-bottom:1.3px solid #666;position:relative}
.burger:after{content:"";position:absolute;left:0;right:0;top:1.6px;border-top:1.3px solid #666}
.group-title{position:absolute;left:64px;top:50px;font-size:12.5px;font-weight:700}
.claims{position:absolute;left:64px;top:75px;font-size:5.8px;line-height:10px}
.claims span{color:#999}
.company-card{position:absolute;top:137px;width:101px;height:96px;border:1px solid var(--line);background:#fff}
.company-card .photo{height:60px}
.company-card .name{position:absolute;left:0;right:0;bottom:0;height:35px;border-left:2px solid;display:flex;align-items:center;justify-content:center;gap:3px;font-size:7px;font-weight:600;white-space:nowrap}
.company-card .name i{width:7px;height:7px;display:block}
.photo-desk{background:linear-gradient(160deg,#5b6470,#8a6a4b 60%,#3c2f26)}
.photo-paper{background:linear-gradient(160deg,#b8c0c8,#e9ecef 60%,#9aa3ab)}
.photo-building{background:linear-gradient(100deg,var(--sky1),var(--sky2) 35%,var(--facade) 55%,#9aa4ae)}
.photo-aerial{background:linear-gradient(140deg,var(--aerial1),#8aa067 45%,var(--aerial2))}
.photo-site{background:linear-gradient(150deg,#8f8a7c,#b9a989 50%,#7a8a66)}
.label{position:absolute;font-size:6px;top:369px}
.page{position:absolute;top:383px;width:325px;border:1px solid var(--line);background:#fff;overflow:hidden}
.page .hero{position:absolute;left:33px;top:31px;width:259px;height:95px}
.page .hero-bar{position:absolute;left:33px;top:126px;width:259px;height:3px;background:var(--green)}
.h1{position:absolute;left:33px;top:136px;font-size:9.8px;font-weight:700}
.h2{position:absolute;left:33px;font-size:6.6px;font-weight:700}
.txt{position:absolute;left:33px;font-size:4.7px;line-height:8px}
.rule{position:absolute;left:33px;width:259px;border-top:0.8px solid var(--line)}
.tiles{position:absolute;left:33px;top:233px;width:259px;display:flex;gap:4px}
.tile{width:48.6px}
.tile .box{height:35px;background:var(--tile);display:flex;align-items:center;justify-content:center}
.tile .box.active{background:var(--green)}
.tile p{font-size:4.2px;line-height:5.2px;margin-top:3px;text-transform:uppercase}
.band{position:absolute;left:33px;top:308px;width:259px;height:17px;background:var(--lime);font-size:6.8px;font-weight:700;padding-left:4px;line-height:18px}
.news-card{position:absolute;background:var(--panel);font-size:4.7px;line-height:8.1px;padding:3px 5px}
.news-card b{display:block;font-weight:700}
.news-card .pic{height:33px;margin:3px 0 4px}
.arrow-l:after,.arrow-r:after{content:"";position:absolute;top:18px;border:4px solid transparent}
.arrow-l:after{right:-8px;border-left-color:var(--panel)}
.arrow-r:after{left:-8px;border-right-color:var(--panel)}
.vline{position:absolute;width:0.8px;background:var(--line)}
.dot{position:absolute;width:8px;height:8px;border-radius:50%;background:var(--lime)}
.gallery{position:absolute;left:33px;width:259px;display:flex;gap:4px}
.gallery div{flex:1;height:58px}
.footer{position:absolute;left:33px;width:259px;height:56px;background:var(--panel);border-left:1.2px solid var(--green);font-size:3.4px;line-height:5.6px;padding:5px 6px;overflow:hidden}
.footer b{font-weight:700;display:block;margin-bottom:5px}
.footer .copy{position:absolute;left:6px;bottom:4px}
.footer .legal{position:absolute;right:6px;bottom:4px}
.date{position:absolute;left:33px;width:40px;height:17px;border:0.8px solid var(--line);font-size:4.8px;font-weight:700;padding-left:5px;line-height:17px;background:#fff}
.row{position:absolute;left:92px;width:200px;background:var(--panel);font-size:4.7px;line-height:8px;padding:4px 5px}
</style>
</head>
<body>

<section class="screen">
  <svg class="facets" viewBox="0 0 391 252" aria-hidden="true">
    <polygon points="260,0 391,0 391,70" fill="var(--facet)"/>
    <polygon points="0,60 60,120 0,170" fill="var(--facet)"/>
    <polygon points="60,150 120,140 60,252" fill="#f8f8f8"/>
  </svg>
  <div class="brand" style="left:46px;top:14px;font-size:9px"><i style="width:9px;height:9px;background:var(--red)"></i>velunto Holding</div>
  <div class="lang" style="left:309px;top:16px">DE | EN <span class="burger"></span></div>
  <h1 class="group-title">velunto group</h1>
  <div class="claims">
    <div><span>//</span> ENTERPRISE CLOUD BUSINESS</div>
    <div><span>//</span> Seed und Early-Stage Investments in B2B-StartUps mit best-in-class Cloud-Technologien REAL</div>
    <div><span>//</span> ESTATE INVESTMENTS</div>
    <div><span>//</span> FAMILIY OFFICE ADVISORY</div>
  </div>
  <a class="company-card" style="left:40px">
    <div class="photo photo-desk" role="img" aria-label="Foto: Geschäftsgespräch am Holztisch"></div>
    <div class="name" style="border-color:var(--red)"><i style="background:var(--red)"></i>velunto Holding</div>
  </a>
  <a class="company-card" style="left:145px">
    <div class="photo photo-paper" role="img" aria-label="Foto: Hand unterschreibt ein Dokument"></div>
    <div class="name" style="border-color:var(--orange);font-size:6px"><i style="background:var(--orange)"></i>velunto trusted advisors</div>
  </a>
  <a class="company-card" style="left:251px">
    <div class="photo photo-building" role="img" aria-label="Foto: moderne Gebäudefassade vor blauem Himmel"></div>
    <div class="name" style="border-color:var(--green);font-size:6.5px"><i style="background:var(--green)"></i>velutno Real estate</div>
  </a>
</section>

<div class="label" style="left:13px">TIMELINE 1</div>
<div class="label" style="left:354px">TIMELINE 2</div>

<section class="page" style="left:13px;height:763px">
  <svg class="facets" viewBox="0 0 325 763" aria-hidden="true">
    <polygon points="190,0 240,0 240,30" fill="var(--facet)"/>
    <polygon points="0,60 33,80 0,130" fill="var(--facet)"/>
    <polygon points="0,180 33,150 33,260" fill="#f8f8f8"/>
  </svg>
  <div class="brand" style="left:33px;top:8px;font-size:8.5px"><i style="width:9px;height:9px"></i>velutno Real estate</div>
  <div class="lang" style="left:258px;top:11px">DE | EN <span class="burger"></span></div>
  <div class="hero photo-building" role="img" aria-label="Foto: Fassade eines modernen Wohngebäudes vor blauem Himmel"></div>
  <div class="hero-bar"></div>
  <h1 class="h1">velutno real estate GmbH</h1>
  <h2 class="h2" style="top:161px">WER SIND WIR?</h2>
  <p class="txt" style="top:171px">Wir sind ein Unternehmen velunto group und entwickeln, bauen, investieren und verwalten<br>Wohn- und Gewerbeimmobilien.</p>
  <div class="rule" style="top:199px"></div>
  <h2 class="h2" style="top:210px">WAS TUN WIR?</h2>
  <p class="txt" style="top:221px">WIR BRINGEN KOMPETENZEN ZUSAMMEN</p>
  <div class="tiles">
    <div class="tile"><div class="box active"><svg width="22" height="20" viewBox="0 0 22 20" fill="none" stroke="#333" stroke-width="0.8"><path d="M2 9 L10 2 L18 9 M4 8 V18 H12"/><circle cx="16" cy="14" r="4"/><text x="14.4" y="16" font-size="5" fill="#333" stroke="none">$</text></svg></div><p>Projektinvestment</p></div>
    <div class="tile"><div class="box"><svg width="22" height="20" viewBox="0 0 22 20" fill="none" stroke="#333" stroke-width="0.8"><rect x="2" y="5" width="16" height="13"/><path d="M5 15 V10 H9 V15 M11 15 V8 H15 V15 M14 5 L19 1"/></svg></div><p>Projekt-<br>entwicklung</p></div>
    <div class="tile"><div class="box"><svg width="22" height="20" viewBox="0 0 22 20" fill="none" stroke="#333" stroke-width="0.8"><rect x="2" y="2" width="18" height="12"/><path d="M11 14 V18 M13 12 V8 M16 12 V6"/><circle cx="11" cy="18.5" r="1"/><text x="4" y="11" font-size="7" fill="#333" stroke="none">$</text></svg></div><p>Projektplanung<br>und Realisierung<br>Asset-Management</p></div>
    <div class="tile"><div class="box"><svg width="22" height="20" viewBox="0 0 22 20" fill="none" stroke="#333" stroke-width="0.8"><path d="M6 8 L11 3 L16 8 V12 H6 Z M2 14 H8 L13 16 L19 13 L13 18 H2"/></svg></div><p>Immobilien-<br>management Family</p></div>
    <div class="tile"><div class="box"><svg width="22" height="20" viewBox="0 0 22 20" fill="none" stroke="#333" stroke-width="0.8"><path d="M2 9 L10 2 L18 9 M4 8 V18 H12"/><circle cx="16" cy="14" r="3"/><circle cx="16" cy="14" r="1"/></svg></div><p>Immobilien-<br>dienstleistungen</p></div>
  </div>
  <div class="rule" style="top:300px"></div>
  <div class="band">PROJEKT SOMMERWIESEN, BRANDTAL</div>
  <p class="txt" style="top:330px">Errichtung eines Campus als neuer Firmensitz der nimbusfeld GmbH und den anderen Unternehmen<br>der velunto group</p>
  <h2 class="h2" style="top:360px;left:34px">NEWS</h2>
  <div class="vline" style="left:162px;top:375px;height:230px"></div>
  <div class="news-card arrow-l" style="left:34px;top:375px;width:113px;height:45px"><b>Juni 2019</b>Vorstellung des Projektes im Gemeinderat der Stadt Brandtal</div>
  <div class="dot" style="left:158px;top:393px"></div>
  <div class="dot" style="left:158px;top:413px"></div>
  <div class="news-card arrow-r" style="left:179px;top:383px;width:113px;height:85px"><b>Juli 2019</b><div class="pic photo-aerial" role="img" aria-label="Luftbild des Projektgeländes mit Grünflächen"></div>Gemeinderat der Stadt Brandtal befürwortet mit deutlicher Mehrheit unser vorgeschla-genes Immobilienprojekt auf den Sommer-wiesen</div>
  <div class="news-card arrow-l" style="left:34px;top:445px;width:113px;height:98px"><b>September 2019</b>Lorem ipsum dolor sit amet, consetetur sadipscing elitr, sed diam nonumy eirmod tempor invidunt ut labore et dolore magna aliquyam erat, sed diam voluptua. Lorem ipsum dolor sit amet, consetetur sadipscing elitr, sed diam nonumy eirmod tempor invidunt ut labore et dolore magna aliquyam erat, sed diam voluptua. At vero eos et accusam et justo duo dolores et ea rebum.</div>
  <div class="dot" style="left:158px;top:463px"></div>
  <div class="news-card arrow-r" style="left:179px;top:503px;width:113px;height:70px"><b>Oktober 2019</b>Lorem ipsum dolor sit amet, consetetur sadipscing elitr, sed diam nonumy eirmod tempor invidunt ut labore et dolore magna aliquyam erat, sed diam voluptua. At vero eos et accusam et justo duo dolores et ea rebum.</div>
  <div class="dot" style="left:158px;top:525px"></div>
  <div class="news-card arrow-l" style="left:34px;top:553px;width:113px;height:52px"><b>Dezember 2019</b>Lorem ipsum dolor sit amet, consetetur sadipscing elitr, sed diam nonumy eirmod tempor invidunt ut labore et dolore magna aliquyam erat, sed diam voluptua.</div>
  <div class="dot" style="left:158px;top:571px"></div>
  <h2 class="h2" style="top:625px;left:34px">BILDER</h2>
  <div class="gallery" style="top:636px">
    <div class="photo-aerial" role="img" aria-label="Luftbild des Geländes mit Bäumen und Wiesen"></div>
    <div class="photo-site" role="img" aria-label="Luftbild der Baustelle in der Stadt"></div>
    <div class="photo-aerial" role="img" aria-label="Luftbild der Baufläche mit Umgebung"></div>
  </div>
  <footer class="footer" style="top:707px">
    <b>velutno real estate GmbH</b>
    Lindenweg 4<br>77000 Brandtal<br>kontakt@velunto-beispiel.de<br>+49 (000) 123 456 78
    <span class="copy">© 2020 by velunto holding GmbH</span>
    <span class="legal">Impressum &nbsp;|&nbsp; Datenschutz</span>
  </footer>
</section>

<section class="page" style="left:354px;height:718px">
  <svg class="facets" viewBox="0 0 325 718" aria-hidden="true">
    <polygon points="190,0 240,0 240,30" fill="var(--facet)"/>
    <polygon points="0,60 33,80 0,130" fill="var(--facet)"/>
    <polygon points="0,180 33,150 33,260" fill="#f8f8f8"/>
  </svg>
  <div class="brand" style="left:33px;top:8px;font-size:8.5px"><i style="width:9px;height:9px"></i>velutno Real estate</div>
  <div class="lang" style="left:258px;top:11px">DE | EN <span class="burger"></span></div>
  <div class="hero photo-building" role="img" aria-label="Foto: Fassade eines modernen Wohngebäudes vor blauem Himmel"></div>
  <div class="hero-bar"></div>
  <h1 class="h1">velutno real estate GmbH</h1>
  <h2 class="h2" style="top:161px">WER SIND WIR?</h2>
  <p class="txt" style="top:171px">Wir sind ein Unternehmen velunto group und entwickeln, bauen, investieren und verwalten<br>Wohn- und Gewerbeimmobilien.</p>
  <div class="rule" style="top:199px"></div>
  <h2 class="h2" style="top:210px">WAS TUN WIR?</h2>
  <p class="txt" style="top:221px">WIR BRINGEN KOMPETENZEN ZUSAMMEN</p>
  <div class="tiles">
    <div class="tile"><div class="box active"><svg width="22" height="20" viewBox="0 0 22 20" fill="none" stroke="#333" stroke-width="0.8"><path d="M2 9 L10 2 L18 9 M4 8 V18 H12"/><circle cx="16" cy="14" r="4"/><text x="14.4" y="16" font-size="5" fill="#333" stroke="none">$</text></svg></div><p>Projektinvestment</p></div>
    <div class="tile"><div class="box"><svg width="22" height="20" viewBox="0 0 22 20" fill="none" stroke="#333" stroke-width="0.8"><rect x="2" y="5" width="16" height="13"/><path d="M5 15 V10 H9 V15 M11 15 V8 H15 V15 M14 5 L19 1"/></svg></div><p>Projekt-<br>entwicklung</p></div>
    <div class="tile"><div class="box"><svg width="22" height="20" viewBox="0 0 22 20" fill="none" stroke="#333" stroke-width="0.8"><rect x="2" y="2" width="18" height="12"/><path d="M11 14 V18 M13 12 V8 M16 12 V6"/><circle cx="11" cy="18.5" r="1"/><text x="4" y="11" font-size="7" fill="#333" stroke="none">$</text></svg></div><p>Projektplanung<br>und Realisierung<br>Asset-Management</p></div>
    <div class="tile"><div class="box"><svg width="22" height="20" viewBox="0 0 22 20" fill="none" stroke="#333" stroke-width="0.8"><path d="M6 8 L11 3 L16 8 V12 H6 Z M2 14 H8 L13 16 L19 13 L13 18 H2"/></svg></div><p>Immobilien-<br>management Family</p></div>
    <div class="tile"><div class="box"><svg width="22" height="20" viewBox="0 0 22 20" fill="none" stroke="#333" stroke-width="0.8"><path d="M2 9 L10 2 L18 9 M4 8 V18 H12"/><circle cx="16" cy="14" r="3"/><circle cx="16" cy="14" r="1"/></svg></div><p>Immobilien-<br>dienstleistungen</p></div>
  </div>
  <div class="rule" style="top:300px"></div>
  <div class="band">PROJEKT SOMMERWIESEN, BRANDTAL</div>
  <p class="txt" style="top:330px">Errichtung eines Campus als neuer Firmensitz der nimbusfeld GmbH und den anderen Unternehmen<br>der velunto group</p>
  <h2 class="h2" style="top:360px;left:34px">NEWS</h2>
  <div class="vline" style="left:82px;top:373px;height:190px"></div>
  <div class="date" style="top:373px">23.06.2019</div><div class="dot" style="left:78px;top:378px"></div>
  <div class="row" style="top:373px;height:29px">Vorstellung des Projektes im Gemeinderat der Stadt Brandtal</div>
  <div class="date" style="top:406px">10.07.2019</div><div class="dot" style="left:78px;top:410px"></div>
  <div class="row" style="top:406px;height:28px">Gemeinderat der Stadt Brandtal befürwortet mit deutlicher Mehrheit unser vorgeschlagenes Immobilienprojekt auf den Sommerwiesen</div>
  <div class="date" style="top:438px">21.08.2019</div><div class="dot" style="left:78px;top:443px"></div>
  <div class="row" style="top:438px;height:51px">Lorem ipsum dolor sit amet, consetetur sadipscing elitr, sed diam nonumy eirmod tempor invidunt ut labore et dolore magna aliquyam erat, sed diam voluptua. Lorem ipsum dolor sit amet, consetetur sadipscing elitr, sed diam nonumy eirmod tempor invidunt ut labore et dolore magna aliquyam erat, sed diam voluptua. At vero eos et accusam et justo duo dolores et ea rebum.</div>
  <div class="date" style="top:493px">12.01.2020</div><div class="dot" style="left:78px;top:498px"></div>
  <div class="row" style="top:493px;height:36px">Lorem ipsum dolor sit amet, consetetur sadipscing elitr, sed diam nonumy eirmod tempor invidunt ut labore et dolore magna aliquyam erat, sed diam voluptua. At vero eos et accusam et justo duo dolores et ea rebum.</div>
  <div class="date" style="top:533px">14.02.2020</div><div class="dot" style="left:78px;top:538px"></div>
  <div class="row" style="top:533px;height:29px">Lorem ipsum dolor sit amet, consetetur sadipscing elitr, sed diam nonumy eirmod tempor invidunt ut labore et dolore magna aliquyam erat.</div>
  <h2 class="h2" style="top:580px;left:34px">BILDER</h2>
  <div class="gallery" style="top:591px">
    <div class="photo-aerial" role="img" aria-label="Luftbild des Geländes mit Bäumen und Wiesen"></div>
    <div class="photo-site" role="img" aria-label="Luftbild der Baustelle in der Stadt"></div>
    <div class="photo-aerial" role="img" aria-label="Luftbild der Baufläche mit Umgebung"></div>
  </div>
  <footer class="footer" style="top:662px">
    <b>velutno real estate GmbH</b>
    Lindenweg 4<br>77000 Brandtal<br>kontakt@velunto-beispiel.de<br>+49 (000) 123 456 78
    <span class="copy">© 2020 by velunto holding GmbH</span>
    <span class="legal">Impressum &nbsp;|&nbsp; Datenschutz</span>
  </footer>
</section>

</body>
</html>
```